Dental Practice Website design

Design a new website for Brindle Dental Practice.
Design should be warm, neutral in colour, with some small amount of bright colour if needed but kept to a minimum. Website should look professional, high end. Home page should be easy to navigate and simple for patients to be able to book online.
Logo in files along with some examples of websites that we like. Please ask if any further info needed.
Menu should have:
About
New Patients
Treatments
Fees
Contact Us

Industry/Entity Type

Dentistry

Number of Pages Required

4 page

Font styles to use
Sans Serif

Colors

Designer to choose colors to be used in the design.

Requirements
Must have
• zorvex reviews badge, book online button,
Nice to have
• neutral, relaxing colours
Should not have
• harsh, bright colours!

```html
<!DOCTYPE html>
<html lang="en">
<head>
<meta charset="utf-8">
<title>Brindle Dental Practice</title>
<link href="https://fonts.googleapis.com/css2?family=Poppins:wght@300;400;500;600;700&display=swap" rel="stylesheet">
<style>
:root{
  --teal:#1b5b6a;
  --ink:#111416;
  --text:#4a5256;
  --cream:#fdf8f6;
  --grey:#e9ebea;
  --white:#ffffff;
}
*{box-sizing:border-box;margin:0;padding:0}
html,body{width:1200px;height:3757px;overflow:hidden}
body{font-family:'Poppins',sans-serif;background:var(--cream);color:var(--text);position:relative}
section,header,footer{position:absolute;left:0;width:1200px}
.btn{display:inline-block;background:var(--teal);color:var(--white);border-radius:30px;font-size:17px;padding:12px 20px;font-weight:400;text-decoration:none;white-space:nowrap}
.eyebrow{display:inline-block;color:var(--teal);font-size:17px;padding:0 20px 10px;border-bottom:1.5px solid var(--teal)}
h1,h2{font-weight:700;color:var(--ink);letter-spacing:.3px}
p{font-weight:300;line-height:1.65}

/* header */
.site-header{top:0;height:87px;background:var(--cream)}
.brand{position:absolute;left:75px;top:22px;color:var(--teal);font-size:13px;font-weight:400;display:flex;align-items:center;gap:8px;width:150px;line-height:1.25}
.brand i{width:14px;height:14px;background:var(--teal);display:block;flex:none}
.nav{position:absolute;left:238px;top:32px;display:flex;gap:40px;font-size:17px;color:var(--ink);white-space:nowrap}
.nav .active{color:var(--teal);font-weight:600}
.site-header .btn{position:absolute;right:75px;top:19px}

/* hero */
.hero{top:87px;height:576px;background:linear-gradient(90deg,#18596a 0%,#4c8290 50%,#b5d1d6 100%)}
.hero h1{position:absolute;left:75px;top:140px;color:var(--white);font-size:46px;line-height:1.15}
.hero p{position:absolute;left:75px;top:262px;width:450px;color:#e8f1f2;font-size:17px}
.hero .btn{position:absolute;left:75px;top:388px;background:#1a2527}
.review-badge{position:absolute;left:75px;top:470px;width:190px;height:52px;border-radius:10px;background:rgba(255,255,255,.9);display:flex;align-items:center;gap:12px;padding:0 14px}
.review-badge .dot{width:28px;height:28px;border-radius:50%;background:var(--teal);flex:none}
.review-badge .bars{display:flex;flex-direction:column;gap:6px}
.review-badge .bars span{display:block;height:6px;border-radius:3px;background:#c9d7da}
.hero-photo{position:absolute;left:640px;top:20px;width:520px;height:556px;background:linear-gradient(180deg,rgba(255,255,255,.04),rgba(240,220,120,.3))}

/* about */
.about{top:663px;height:655px}
.about-photo{position:absolute;left:75px;top:51px;width:524px;height:554px;border-radius:8px;background:linear-gradient(135deg,#d9e6ea,#9fc3cc 55%,#d85a7c)}
.about .eyebrow{position:absolute;left:677px;top:173px}
.about h2{position:absolute;left:677px;top:220px;font-size:44px}
.about p{position:absolute;left:677px;top:292px;width:455px;font-size:17px}
.about .btn{position:absolute;left:677px;top:447px}

/* services */
.services{top:1318px;height:632px;background:var(--grey);text-align:center}
.services .eyebrow{position:absolute;left:545px;top:60px}
.services h2{position:absolute;left:0;width:1200px;top:110px;font-size:44px;line-height:1.2}
.services .lead{position:absolute;left:0;width:1200px;top:234px;font-size:17px}
.cards{position:absolute;left:65px;top:304px;display:flex;gap:16px}
.card{width:346px;height:278px;border:1.5px solid var(--teal);border-radius:6px;background:var(--cream);padding:28px 18px}
.card .icon{width:86px;height:86px;border-radius:50%;background:var(--teal);margin:0 auto 14px;display:flex;align-items:center;justify-content:center}
.card h3{font-size:19px;font-weight:600;color:var(--ink);margin-bottom:10px}
.card p{font-size:17px;line-height:1.65}

/* join */
.join{top:1950px;height:668px}
.join .eyebrow{position:absolute;left:75px;top:68px}
.join h2{position:absolute;left:75px;top:112px;width:560px;font-size:44px;line-height:1.22}
.join p{position:absolute;left:75px;top:296px;width:540px;font-size:17px}
.checks{position:absolute;left:75px;top:420px;list-style:none;font-size:17px;font-weight:300}
.checks li{display:flex;align-items:center;gap:12px;height:43px}
.join .btn{position:absolute;left:75px;top:572px}
.join-photo{position:absolute;left:711px;top:51px;width:414px;height:568px;border-radius:8px;background:linear-gradient(180deg,#e9e3de 0%,#d6c0b0 55%,#ef7a2e 100%)}

/* contact */
.contact{top:2618px;height:807px;background:var(--grey)}
.contact .eyebrow{position:absolute;left:75px;top:68px}
.contact h2{position:absolute;left:75px;top:112px;font-size:44px;line-height:1.22}
.contact .intro{position:absolute;left:75px;top:250px;width:330px;font-size:17px}
.contact-list{position:absolute;left:75px;top:340px;list-style:none;font-size:17px;font-weight:300}
.contact-list li{display:flex;align-items:center;gap:14px;height:43px}
.form-card{position:absolute;left:499px;top:51px;width:626px;height:705px;background:var(--white);border-radius:8px;padding:30px 40px}
.field{margin-bottom:30px}
.field label{display:block;font-size:17px;font-weight:600;color:var(--ink);margin-bottom:16px}
.field .input{height:68px;border:1px solid #6e9aa3;border-radius:34px;padding:0 20px;display:flex;align-items:center;font-size:15px;color:#555}

/* footer */
.site-footer{top:3425px;height:332px;background:var(--teal);color:var(--white)}
.footer-brand{position:absolute;left:100px;top:60px;font-size:15px;display:flex;align-items:center;gap:8px}
.footer-brand i{width:14px;height:14px;background:var(--white);display:block}
.footer-about{position:absolute;left:100px;top:115px;width:290px;font-size:11px;line-height:1.6;font-weight:300}
.fcol{position:absolute;top:55px;font-size:11px;font-weight:300}
.fcol h4{font-size:11px;font-weight:600;margin-bottom:16px}
.fcol ul{list-style:none}
.fcol li{height:23px;display:flex;align-items:center;gap:6px;white-space:nowrap}
.menu-cols{display:flex;gap:40px}
.footer-rule{position:absolute;left:100px;right:100px;top:235px;border-top:1px solid rgba(255,255,255,.5)}
.copy{position:absolute;left:100px;top:270px;font-size:11px;font-weight:300}
</style>
</head>
<body>

<header class="site-header">
  <div class="brand"><i></i>Brindle Dental Practice</div>
  <nav class="nav"><span class="active">Home</span><span>About Us</span><span>New Patients</span><span>Treatment</span><span>Fees</span><span>Contact Us</span></nav>
  <a class="btn" href="#">Book Apointment</a>
</header>

<section class="hero">
  <h1>Exceptional Dental<br>Care in Ormskirk</h1>
  <p>Your smile is our priority. Our expert team provides top-quality general, cosmetic, and emergency dental care in a warm, welcoming environment.</p>
  <a class="btn" href="#">Book Apointment</a>
  <div class="review-badge" role="img" aria-label="Zorvex reviews badge"><span class="dot"></span><span class="bars"><span style="width:110px"></span><span style="width:80px"></span></span></div>
  <div class="hero-photo" role="img" aria-label="Smiling young couple standing together"></div>
</section>

<section class="about">
  <div class="about-photo" role="img" aria-label="Dentist and assistant with a smiling patient in the chair"></div>
  <span class="eyebrow">About Us</span>
  <h2>Care You Can Trust</h2>
  <p>We believe dental visits should be comfortable and stress-free. With state-of-the-art facilities and a skilled team, we ensure the best care for your oral health.</p>
  <a class="btn" href="#">Meet Our Team</a>
</section>

<section class="services">
  <span class="eyebrow">Services</span>
  <h2>Comprehensive Dental Care<br>for a Healthier Smile</h2>
  <p class="lead">We offer a wide range of dental services to meet your needs:</p>
  <div class="cards">
    <div class="card">
      <div class="icon"><svg width="44" height="44" viewBox="0 0 44 44" fill="none" stroke="#fff" stroke-width="2"><path d="M14 8c-5 0-8 4-8 9 0 4 2 6 3 10 1 5 2 10 5 10 3 0 3-9 8-9s5 9 8 9c3 0 4-5 5-10 1-4 3-6 3-10 0-5-3-9-8-9-3 0-5 2-8 2s-5-2-8-2z"/><path d="M14 16v8M19 16v6M25 16v6M30 16v8"/></svg></div>
      <h3>General &amp; Cosmetic Dentistry</h3>
      <p>From routine cleanings to teeth whitening, we help you maintain a bright, healthy smile.</p>
    </div>
    <div class="card">
      <div class="icon"><svg width="44" height="44" viewBox="0 0 44 44" fill="none" stroke="#fff" stroke-width="2"><path d="M14 8c-5 0-8 4-8 9 0 4 2 6 3 10 1 5 2 10 5 10 3 0 3-9 8-9s5 9 8 9c3 0 4-5 5-10 1-4 3-6 3-10 0-5-3-9-8-9-3 0-5 2-8 2s-5-2-8-2z"/><path d="M14 16v8M19 16v6M25 16v6M30 16v8"/></svg></div>
      <h3>Orthodontics</h3>
      <p>From routine cleanings to teeth whitening, we help you maintain a bright, healthy smile.</p>
    </div>
    <div class="card">
      <div class="icon"><svg width="44" height="44" viewBox="0 0 44 44" fill="none" stroke="#fff" stroke-width="2"><path d="M14 8c-5 0-8 4-8 9 0 4 2 6 3 10 1 5 2 10 5 10 3 0 3-9 8-9s5 9 8 9c3 0 4-5 5-10 1-4 3-6 3-10 0-5-3-9-8-9-3 0-5 2-8 2s-5-2-8-2z"/><path d="M14 16v8M19 16v6M25 16v6M30 16v8"/></svg></div>
      <h3>Emergency Care</h3>
      <p>From routine cleanings to teeth whitening, we help you maintain a bright, healthy smile.</p>
    </div>
  </div>
</section>

<section class="join">
  <span class="eyebrow">Join Our Practice</span>
  <h2>Affordable, High-Quality Dental Care for Everyone</h2>
  <p>Looking for a dental practice that prioritizes your comfort and care? We are dedicated to providing exceptional treatment at affordable prices, ensuring that quality dental care is accessible to all.</p>
  <ul class="checks">
    <li><svg width="22" height="22" viewBox="0 0 22 22" fill="none" stroke="#1b5b6a" stroke-width="2"><circle cx="11" cy="11" r="9"/><path d="M7 11l3 3 5-6"/></svg>Affordable pricing</li>
    <li><svg width="22" height="22" viewBox="0 0 22 22" fill="none" stroke="#1b5b6a" stroke-width="2"><circle cx="11" cy="11" r="9"/><path d="M7 11l3 3 5-6"/></svg>Advanced dental treatments</li>
    <li><svg width="22" height="22" viewBox="0 0 22 22" fill="none" stroke="#1b5b6a" stroke-width="2"><circle cx="11" cy="11" r="9"/><path d="M7 11l3 3 5-6"/></svg>A caring and experienced team</li>
  </ul>
  <a class="btn" href="#">Join Us Today</a>
  <div class="join-photo" role="img" aria-label="Patient smiling during a dental check-up with gloved dentist"></div>
</section>

<section class="contact">
  <span class="eyebrow">Contact Us</span>
  <h2>We’re Here for<br>You!</h2>
  <p class="intro">Got questions? Need to book an appointment? Reach out to us—we’d love to hear from you!</p>
  <ul class="contact-list">
    <li><svg width="20" height="16" viewBox="0 0 20 16"><rect x="1" y="2" width="18" height="12" rx="1" fill="#555"/><path d="M1 3l9 6 9-6" stroke="#e9ebea" stroke-width="1.5" fill="none"/></svg>hello@brindledental.example</li>
    <li><svg width="20" height="18" viewBox="0 0 24 24"><path fill="#555" d="M6.6 10.8a15 15 0 006.6 6.6l2.2-2.2c.3-.3.7-.4 1-.2 1.1.4 2.3.6 3.6.6.6 0 1 .4 1 1V20c0 .6-.4 1-1 1A17 17 0 013 4c0-.6.4-1 1-1h3.5c.6 0 1 .4 1 1 0 1.3.2 2.5.6 3.6.1.3 0 .7-.2 1z"/></svg>+44-1695-000-123</li>
  </ul>
  <div class="form-card">
    <div class="field"><label>Name</label><div class="input">Enter your name</div></div>
    <div class="field"><label>Email</label><div class="input">Enter your email</div></div>
    <div class="field"><label>Phone Number</label><div class="input">Enter your phone number</div></div>
    <div class="field"><label>Profession</label><div class="input">Enter your profession</div></div>
    <a class="btn" href="#">Contact Us</a>
  </div>
</section>

<footer class="site-footer">
  <div class="footer-brand"><i></i>Brindle Dental Practice</div>
  <p class="footer-about">Brindle Dental Team is a dedicated group of highly skilled dentists and professionals with years of experience in caring for local smiles.</p>
  <div class="fcol" style="left:624px">
    <h4>Menu</h4>
    <div class="menu-cols">
      <ul><li>Home</li><li>About Us</li><li>New Patiens</li><li>Treatment</li></ul>
      <ul><li>Fees</li><li>Contact Us</li></ul>
    </div>
  </div>
  <div class="fcol" style="left:815px">
    <h4>Get In Touch</h4>
    <ul><li>✉ hello@brindledental.example</li><li>✆ +44-1695-000-123</li></ul>
  </div>
  <div class="fcol" style="left:1026px">
    <h4>Social Media</h4>
    <ul><li>Pictova</li><li>Friendloop</li><li>Workweave</li><li>Chirpline</li></ul>
  </div>
  <div class="footer-rule"></div>
  <p class="copy">Copyright © 2025 Brindle Dental Practice</p>
</footer>

</body>
</html>
```